HIGH-END ANTI AGING START-UP NEEDS DOCUMENT/LETTERHEAD DESIGN!!!!

We are a high end anti-aging and health start-up catering to clients in Stamford and NYC. We just did a logo redesign and are now looking for a letter head design that we can use IN GOOGLE DOCS for marwickcaregroup.example clients. We are REALLY EXCITED to see what you can show us!!!!!!!! We need something sophisticated and MODERN! Thanks so much!

Target Market(s)

High end, boutique medical clients. Our clientele is fairly high profile and we need a sleek, sophisticated letter head to put on all of our marketing materials and medical forms as well.

Industry/Entity Type

Medical

Font styles to use
Serif
Sans Serif

Colors
0255a3
ffffff
00a990
1b1b1b
919191

Requirements
Must have
• Must have the logo and "Marwick Care Group" written somewhere. Must have our URL www.marwickcaregroup.example.
Nice to have
• office phone number (203) 555-0147
Should not have
• Colors outside of our logo colors + grey + black

```html
<!DOCTYPE html>
<html lang="en">
<head>
<meta charset="utf-8">
<title>Marwick Care Group – Letterhead</title>
<link rel="stylesheet" href="https://fonts.googleapis.com/css2?family=Arimo:wght@400;700&family=Libre+Baskerville&display=swap">
<style>
  :root {
    --backdrop: #ececec;
    --paper: #ffffff;
    --brand-green: #0b8a43;
    --brand-blue: #0255a3;
    --ink: #1b1b1b;
    --muted: #919191;
    --on-green: #ffffff;
  }
  * { box-sizing: border-box; margin: 0; padding: 0; }
  html, body { width: 1200px; height: 795px; overflow: hidden; }
  body {
    background: var(--backdrop);
    font-family: "Arimo", Arial, sans-serif;
    color: var(--ink);
    position: relative;
  }
  .letterhead {
    position: absolute;
    left: 333px; top: 20px;
    width: 534px; height: 755px;
    background: var(--paper);
    box-shadow: 0 2px 10px rgba(0,0,0,0.12);
    overflow: hidden;
  }
  .brand {
    position: absolute; left: 58px; top: 48px;
    display: flex; align-items: center; gap: 8px;
  }
  .brand-dot {
    width: 26px; height: 26px; border-radius: 50%;
    background: var(--brand-green);
  }
  .brand-name {
    font-size: 11px; font-weight: 700; letter-spacing: 1.2px;
    color: var(--brand-blue); text-transform: uppercase;
  }
  .recipient {
    position: absolute; left: 58px; top: 150px;
    font-size: 8px; line-height: 1.3;
  }
  .recipient-name { font-weight: 700; font-size: 8.5px; text-transform: uppercase; }
  .letter-body {
    position: absolute; left: 100px; top: 200px; width: 380px;
    font-size: 8.4px; line-height: 1.55;
  }
  .letter-body p { margin-bottom: 14px; }
  .closing { margin-top: -6px; }
  .signature-mark {
    width: 110px; height: 34px; margin-top: 8px;
    background: linear-gradient(90deg, #e6e6e6, #f4f4f4);
    border-radius: 4px;
  }
  .signer { margin-top: 4px; font-size: 8.4px; }
  .office-title {
    position: absolute; left: 300px; top: 610px;
    font-family: "Libre Baskerville", Georgia, serif;
    font-size: 11.5px; letter-spacing: 0.5px;
    color: var(--ink); text-transform: uppercase;
  }
  .footer-band {
    position: absolute; left: 0; bottom: 0; width: 534px; height: 120px;
  }
  .footer-band svg { position: absolute; inset: 0; }
  .band-ornament {
    position: absolute; right: 0; bottom: 110px;
    width: 70px; height: 34px;
    background: linear-gradient(180deg, rgba(11,138,67,0.15), var(--brand-green));
  }
  .office {
    position: absolute; color: var(--on-green);
    font-size: 8.6px; line-height: 1.35;
  }
  .office-label { font-weight: 700; }
  .office-ny { left: 30px; bottom: 16px; }
  .office-ct { left: 172px; bottom: 16px; }
  .office-divider {
    position: absolute; left: 155px; bottom: 14px;
    width: 1px; height: 36px; background: var(--on-green);
  }
  .contact {
    position: absolute; right: 26px; bottom: 22px;
    color: var(--on-green); font-size: 8px; line-height: 1.45;
  }
  .contact-cta { font-weight: 700; }
</style>
</head>
<body>
  <article class="letterhead">
    <header class="brand">
      <span class="brand-dot"></span>
      <span class="brand-name">Marwick Care Group</span>
    </header>

    <address class="recipient" style="font-style:normal">
      <div class="recipient-name">Clara Whitfield</div>
      <div>Street Name,City Name.</div>
      <div>Zip Coad 0000</div>
    </address>

    <section class="letter-body">
      <p>Lorem Ipsum is simply dummy text of the printing and typesetting industry. Lorem Ipsum has been the industry's standard dummy text ever since the 1500s, when an unknown printer took a galley of type and scrambled it to make a type specimen book. It has survived not only five centuries, but also the leap into electronic typesetting, remaining essentially unchanged. It was popularised in the 1960s with the release of Letraset sheets containing Lorem Ipsum passages, and more recently with desktop publishing software like Aldus PageMaker including versions of Lorem Ipsum.</p>
      <p>It is a long established fact that a reader will be distracted by the readable content of a page when looking at its layout. The point of using Lorem Ipsum is that it has a more-or-less normal distribution of letters, as opposed to using 'Content here, content here', making it look like readable English. Many desktop and publishing packages and web page editors now use Lorem Ipsum as their default model text, and a search for 'lorem ipsum' will uncover many web sites still in their infancy. Various versions have evolved over the years, sometimes by accident, sometimes on purpose (injected humour and the like).</p>
      <div class="closing">Regards,</div>
      <div class="signature-mark" role="img" aria-label="Handwritten signature of Evan Hale"></div>
      <div class="signer">Evan Hale</div>
    </section>

    <div class="office-title">Marwick Care Group</div>

    <footer class="footer-band">
      <div class="band-ornament" role="img" aria-label="Decorative row of pine trees"></div>
      <svg width="534" height="120" viewBox="0 0 534 120" aria-hidden="true">
        <path d="M0 58 L350 58 L350 12 L534 12 L534 120 L0 120 Z" fill="var(--brand-green)"/>
      </svg>
      <div class="office office-ny">
        <div class="office-label">New York Office:</div>
        <div>120 Harbor Lane,</div>
        <div>New York, NY, 10014</div>
      </div>
      <span class="office-divider"></span>
      <div class="office office-ct">
        <div class="office-label">Connecticut Office:</div>
        <div>18 Linden Ave. Suite 300</div>
        <div>Stamford CT, 06901</div>
      </div>
      <div class="contact">
        <div>(203) 555-0147</div>
        <div class="contact-cta">Call For An Appointment!</div>
        <div>www.marwickcaregroup.example</div>
      </div>
    </footer>
  </article>
</body>
</html>
```